Business Card - connecting 2 souls and beggining the journey of self discovery

Logo on the front
with tag line

On the back list of services and contact details

Seminars
workshops
Coaching
podcasts

Daniel Porthwick
Health & Wellbeing Life Coach
0491 372 815
daniel@wovenpathwellness.example
wovenpathwellness.example

Industry/Entity Type

Life Coaching

Contact Information for Business Card

I like the use of colour from the logo to be used. I'm not a fan of white.

Requirements
Must have
• My tagline: The journey home starts with you
Nice to have
• Use of colour that is in the mind body soul logo

```html
<!DOCTYPE html>
<html lang="en">
<head>
<meta charset="utf-8">
<title>Woven Path Wellness — Business Card</title>
<link href="https://fonts.googleapis.com/css2?family=Roboto:wght@300;400;700&family=Montserrat:wght@500&display=swap" rel="stylesheet">
<style>
  :root {
    --backdrop: #262626;
    --card: #fbfbfb;
    --ink: #474747;
    --ink-soft: #555555;
    --tagline: #858585;
    --mark: #e9a06a;
  }
  * { margin: 0; padding: 0; box-sizing: border-box; }
  html, body {
    width: 1200px;
    height: 1096px;
    overflow: hidden;
    background: var(--backdrop);
  }
  .canvas {
    position: relative;
    width: 1200px;
    height: 1096px;
  }
  .card {
    position: absolute;
    width: 550px;
    height: 317px;
    background: var(--card);
    font-family: "Roboto", Arial, sans-serif;
    color: var(--ink);
  }

  /* Reverse side: services + contact */
  .card--back { left: 491px; top: 207px; }
  .services {
    position: absolute;
    top: 48px;
    left: 0;
    width: 100%;
    text-align: center;
    font-weight: 700;
    font-size: 25px;
    letter-spacing: -0.1px;
  }
  .contact {
    position: absolute;
    left: 23px;
    top: 166px;
    list-style: none;
    font-weight: 400;
    font-size: 21px;
    line-height: 26.5px;
    white-space: nowrap;
  }
  .brand--back {
    position: absolute;
    left: 396px;
    top: 158px;
    width: 136px;
    text-align: center;
  }
  .brand--back .brand-dot { width: 100px; height: 100px; margin: 0 auto 10px; }
  .brand--back .brand-name { font-size: 14px; white-space: nowrap; }

  /* Front side: brand + tagline */
  .card--front { left: 198px; top: 566px; }
  .brand--front {
    position: absolute;
    top: 54px;
    left: 0;
    width: 100%;
    text-align: center;
  }
  .brand--front .brand-dot { width: 106px; height: 106px; margin: 0 auto 12px; }
  .brand--front .brand-name { font-size: 19px; }
  .brand-dot {
    border-radius: 50%;
    background: var(--mark);
  }
  .brand-name {
    font-family: "Roboto", Arial, sans-serif;
    font-weight: 400;
    color: var(--ink);
    letter-spacing: 0.3px;
  }
  .tagline {
    position: absolute;
    top: 228px;
    left: 0;
    width: 100%;
    text-align: center;
    font-family: "Montserrat", Arial, sans-serif;
    font-weight: 500;
    font-size: 29px;
    letter-spacing: -1.2px;
    color: var(--tagline);
    white-space: nowrap;
  }
  .website {
    position: absolute;
    top: 282px;
    left: 0;
    width: 100%;
    text-align: center;
    font-weight: 300;
    font-size: 17px;
    color: var(--ink-soft);
  }
</style>
</head>
<body>
<main class="canvas">
  <section class="card card--back" aria-label="Card reverse">
    <h2 class="services">Seminar Workshop Coaching Podcast</h2>
    <ul class="contact">
      <li>Daniel Porthwick</li>
      <li>Health &amp; Wellbeing Life Coach</li>
      <li>0491 372 815</li>
      <li>daniel@wovenpathwellness.example</li>
      <li>wovenpathwellness.example</li>
    </ul>
    <div class="brand brand--back">
      <div class="brand-dot"></div>
      <div class="brand-name">Woven Path Wellness</div>
    </div>
  </section>

  <section class="card card--front" aria-label="Card front">
    <div class="brand brand--front">
      <div class="brand-dot"></div>
      <div class="brand-name">Woven Path Wellness</div>
    </div>
    <p class="tagline">The journey home starts with you</p>
    <p class="website">www.wovenpathwellness.example</p>
  </section>
</main>
</body>
</html>
```